Bourbon Lantern is a speakeasy whiskey and cigar website needing fresh look for product sales

This is a new company just starting out that will be Design needs to be modern edge of prohibition of the 1920's and the speakeasies that were created from them. Needs to include the moonshine runners, stills and whiskey. Also needs to have the sophistication of a speakeasy where gentlemen and now women go to sit in luxury leather chairs with their whiskey and cigar. Lastly my website will not be selling alcohol or cigars. Just higher end accessories and furniture designs in the Bourbon Lantern store that will help the consumer feel like they are back in time while sitting in the comfort of their own speakeasy.

I will attach my current logo but I am open to suggestions to better suit my vision. I do have photos of products that have been purchased to put on website. I am leaving the designs of actual website itself to the designer.

Target Market(s)

21 yrs +; home owners; mature audience; redesign room; cigar accessories; liquor accessories

Industry/Entity Type

home bars, liquor accessories, cigar accessories

Coding

Coded - Design and coding required

Number of Pages Required

1 page

Font styles to use
Serif
Decorative
Script

Colors

Designer to choose colors to be used in the design.

Requirements
Must have
• key words for search engines, eye catching designs matching key words, links to online store and social media
Nice to have
• logo, mixture of retro/old feel with modern day twist; speakeasy/moonshine runners with luxury and class
Should not have
• nudity, XXX, racism

```html
<!DOCTYPE html>
<html lang="en">
<head>
<meta charset="utf-8">
<title>Bourbon Lantern – Speakeasy Bar &amp; Cigar Accessories</title>
<meta name="description" content="Bourbon Lantern sells speakeasy home bar furniture, whiskey accessories and cigar accessories with a 1920s prohibition feel.">
<meta name="keywords" content="speakeasy furniture, home bar, whiskey accessories, cigar accessories, prohibition decor, leather lounge chairs, bourbon decanters">
<link href="https://fonts.googleapis.com/css2?family=Italiana&family=DM+Sans:wght@400;500;600&display=swap" rel="stylesheet">
<style>
:root{
  --ink:#000;
  --paper:#fff;
  --blush:#e3c1b6;
  --rose:#d59b8d;
  --cocoa:#5b4b40;
  --grey:#8a8a8a;
  --line:#3a3a3a;
  --serif:'Italiana',serif;
  --sans:'DM Sans',sans-serif;
}
*{margin:0;padding:0;box-sizing:border-box}
html,body{width:1200px;height:4808px;overflow:hidden}
body{position:relative;background:var(--paper);font-family:var(--sans);color:var(--ink)}
.abs{position:absolute}
.band{position:absolute;left:0;width:1200px}
.dark{background:var(--ink);color:var(--paper)}
.photo{position:absolute}
.serif{font-family:var(--serif);font-weight:400}
.btn{position:absolute;display:flex;align-items:center;justify-content:center;border-radius:20px;font-size:11px;font-weight:500;text-decoration:none}
.btn-blush{background:var(--blush);color:var(--ink)}
.btn-ghost{border:1.5px solid #cfcfcf;background:var(--paper);color:var(--ink)}
.btn-ghost-dark{border:1.5px solid #fff;color:#fff}
.rule{position:absolute;height:1px;background:#555}

/* header */
.brand{position:absolute;left:75px;top:19px}
.brand-ring{width:74px;height:74px;border:1.5px solid var(--blush);border-radius:50%;display:flex;align-items:center;justify-content:center;font-size:10px;color:var(--blush);text-align:center;line-height:1.2;font-weight:500}
.nav a{position:absolute;top:31px;font-size:10px;color:#fff;text-decoration:none;font-weight:500}
.nav-phone{position:absolute;left:850px;top:30px;font-size:11px;color:#fff;display:flex;gap:6px;align-items:center}

/* hero */
.hero-title{left:75px;top:170px;font-size:62px;line-height:72px;color:#fff}
.hero-sub{left:75px;top:340px;font-size:17px;color:#fff}

/* about */
.eyebrow{font-size:10px;color:var(--rose)}
.about-title{left:487px;top:740px;font-size:40px;line-height:50px;width:480px}
.body-copy{font-size:10.5px;line-height:19px;color:#666}

/* collections */
.svc{position:absolute;top:1340px;width:300px;text-align:center}
.svc h3{font-size:13px;font-weight:500;margin-top:14px;color:#fff}
.svc p{font-size:10px;line-height:19px;color:#9a9a9a;margin-top:14px}
.svc .more{font-size:10.5px;color:var(--rose);margin-top:12px;display:block;text-decoration:none}

.section-title{font-size:41px;line-height:46px}

/* testimonial */
.quote{left:474px;top:3205px;width:460px;font-size:13.5px;line-height:22px;color:#fff}
.circle-btn{position:absolute;width:30px;height:30px;border:1px solid #bbb;border-radius:50%;display:flex;align-items:center;justify-content:center}

/* features */
.feat{position:absolute;top:3720px;width:200px;text-align:center;font-size:12.5px}
.feat svg{display:block;margin:0 auto 14px}

/* contact */
.field{position:absolute;background:#fff;font-size:9px;padding:8px 10px;color:#222}

/* footer */
.foot-label{font-size:11px;font-weight:600;color:#fff;display:flex;align-items:center;gap:10px}
.foot-label span{display:block;width:60px;height:1px;background:#777}
.foot-text{font-size:17px;color:#fff;line-height:35px}
.social{position:absolute;top:4654px;width:30px;height:30px;border-radius:50%;background:#2b2b2b}
</style>
</head>
<body>

<!-- header + hero -->
<section class="band dark" style="top:0;height:550px"></section>
<div class="photo" style="left:381px;top:75px;width:819px;height:550px;background:linear-gradient(120deg,#2a1d18 0%,#4b372c 45%,#7a6656 70%,#cfc2ad 100%)" role="img" aria-label="Woman seated in a tufted leather armchair holding a glass"></div>

<div class="brand"><div class="brand-ring">Bourbon<br>Lantern</div></div>
<nav class="nav">
  <a href="#" style="left:381px">Home</a>
  <a href="#" style="left:446px">About Us</a>
  <a href="#" style="left:525px">Shop</a>
  <a href="#" style="left:603px">Collections</a>
  <a href="#" style="left:679px">Reviews</a>
  <a href="#" style="left:756px">Contact Us</a>
</nav>
<div class="nav-phone">
  <svg width="11" height="11" viewBox="0 0 24 24" fill="none" stroke="#fff" stroke-width="2"><path d="M5 3h4l2 5-3 2a12 12 0 0 0 6 6l2-3 5 2v4a2 2 0 0 1-2 2A18 18 0 0 1 3 5a2 2 0 0 1 2-2z"/></svg>
  1 (555) 018-2290
</div>
<a class="btn" href="#" style="left:1000px;top:19px;width:125px;height:37px;background:var(--cocoa);color:#fff">Shop now!</a>

<h1 class="abs serif hero-title">Discover the spirit<br>of the speakeasy</h1>
<p class="abs hero-sub">Bar, cigar and lounge pieces for your home</p>
<a class="btn btn-blush" href="#" style="left:75px;top:394px;width:125px;height:37px">Shop now!</a>

<!-- about -->
<div class="photo" style="left:75px;top:625px;width:306px;height:532px;background:linear-gradient(160deg,#3a2418 0%,#7a4a2c 40%,#1f3b38 75%,#0e1c1e 100%)" role="img" aria-label="Warmly lit home speakeasy lounge with green velvet booths and bar shelves"></div>
<div class="rule" style="left:381px;top:767px;width:62px;background:#333"></div>
<p class="abs eyebrow" style="left:487px;top:719px">About us</p>
<h2 class="abs serif about-title">We bring the roaring twenties back into your home bar</h2>
<p class="abs body-copy" style="left:487px;top:917px;width:500px">Bourbon Lantern curates higher end speakeasy accessories and furniture inspired by prohibition, moonshine runners and hidden copper stills. From leather lounge chairs to crystal decanters and cigar humidors, every piece helps you feel back in time while relaxing in the comfort of your own speakeasy ...</p>
<a class="btn btn-ghost" href="#" style="left:487px;top:1023px;width:125px;height:37px">Visit the store</a>

<!-- collections -->
<section class="band dark" style="top:1157px;height:541px"></section>
<h2 class="abs serif" style="left:0;width:1200px;text-align:center;top:1228px;font-size:42px;color:#fff">Exceptional pieces we offer</h2>
<div class="abs" style="left:414px;top:1325px;width:1px;height:224px;background:var(--line)"></div>
<div class="abs" style="left:784px;top:1325px;width:1px;height:224px;background:var(--line)"></div>

<div class="svc" style="left:81px">
  <svg width="44" height="46" viewBox="0 0 44 46" fill="none" stroke="#fff" stroke-width="1.6"><path d="M10 2v20l-6 10h16l-6-10V2M30 2v18l-6 12h16l-6-12V2M4 32h16M24 32h16M12 32v12M32 32v12"/></svg>
  <h3>Whiskey &amp; Bar Accessories</h3>
  <p>decanters, glassware and copper still pieces<br>that bring prohibition charm to every pour<br>at your home bar...</p>
  <a class="more" href="#">Shop Now ↗</a>
</div>
<div class="svc" style="left:449px">
  <svg width="46" height="46" viewBox="0 0 46 46" fill="none" stroke="#fff" stroke-width="1.6"><rect x="6" y="14" width="34" height="8"/><path d="M10 22v20M36 22v20M10 32h26M16 14V6h14v8M23 2v4"/></svg>
  <h3>Lounge Furniture</h3>
  <p>leather club chairs, bar carts and tables<br>built for a speakeasy room of luxury and<br>class in your own house...</p>
  <a class="more" href="#">Shop Now ↗</a>
</div>
<div class="svc" style="left:818px">
  <svg width="46" height="46" viewBox="0 0 46 46" fill="none" stroke="#fff" stroke-width="1.6"><rect x="4" y="8" width="32" height="34"/><path d="M14 32l4-10L40 2l4 4-20 22zM8 16h14M8 22h8"/></svg>
  <h3>Cigar Accessories</h3>
  <p>humidors, cutters, lighters and ashtrays<br>crafted for the gentleman and lady who<br>enjoy a fine evening smoke...</p>
  <a class="more" href="#">Shop Now ↗</a>
</div>
<a class="btn btn-blush" href="#" style="left:537px;top:1587px;width:125px;height:37px">Shop now!</a>

<!-- rooms -->
<h2 class="abs serif section-title" style="left:200px;top:1770px">Speakeasy rooms we love</h2>
<div class="rule" style="left:0;top:1857px;width:343px;background:#333"></div>
<p class="abs" style="left:381px;top:1850px;font-size:10.5px">Home bars styled by our customers with pieces from the Bourbon Lantern store.</p>

<div class="photo" style="left:200px;top:1892px;width:436px;height:437px;background:linear-gradient(150deg,#2b1a2e 0%,#a05a8c 45%,#d48fc2 70%,#3a2a3a 100%)" role="img" aria-label="Neon-lit bar with pink stools and a wooden counter"></div>
<div class="photo" style="left:649px;top:1892px;width:351px;height:347px;background:linear-gradient(170deg,#5a4420 0%,#a08040 35%,#3c3830 70%,#1c1b1a 100%)" role="img" aria-label="Long marble bar with brass arches and leather stools"></div>
<div class="photo" style="left:649px;top:2254px;width:351px;height:349px;background:linear-gradient(160deg,#231a14 0%,#6b4a30 45%,#a68360 65%,#1d1610 100%)" role="img" aria-label="Dim bar interior with pendant lamps and mirrored shelves"></div>
<div class="photo" style="left:200px;top:2342px;width:436px;height:437px;background:linear-gradient(180deg,#3a3028 0%,#6e5a44 40%,#2e2822 70%,#8a7a62 100%)" role="img" aria-label="Rustic bar with chained shelving of bottles and upholstered chairs"></div>
<div class="photo" style="left:649px;top:2616px;width:351px;height:343px;background:linear-gradient(170deg,#1c1714 0%,#5a4028 40%,#8c6a44 60%,#2a2018 100%)" role="img" aria-label="Bar counter with crystal chandeliers and decanters"></div>
<div class="abs" style="left:649px;top:2959px;width:351px;height:6px;background:var(--blush)"></div>
<a class="btn btn-ghost" href="#" style="left:362px;top:2824px;width:112px;height:36px">View the shop</a>

<!-- testimonials -->
<section class="band dark" style="top:2948px;height:575px"></section>
<div class="abs" style="left:649px;top:2948px;width:351px;height:17px;background:var(--blush)"></div>
<h2 class="abs serif section-title" style="left:200px;top:3040px;color:#fff">Happy clients say</h2>
<div class="rule" style="left:0;top:3124px;width:364px;background:#444"></div>
<div class="photo" style="left:202px;top:3155px;width:180px;height:180px;border-radius:50%;background:radial-gradient(circle at 50% 40%,#8a6a4e 0%,#4a3424 55%,#1e1510 100%)" role="img" aria-label="Portrait of a customer in his home bar"></div>
<p class="abs" style="left:231px;top:3356px;font-size:13px;color:#fff;font-weight:500">Walter Hale</p>
<p class="abs" style="left:231px;top:3377px;font-size:10px;color:#888">Louisville</p>
<svg class="abs" style="left:474px;top:3152px" width="30" height="24" viewBox="0 0 30 24" fill="var(--blush)"><path d="M0 0h12v12l-5 12H2l4-12H0zM16 0h12v12l-5 12h-5l4-12h-6z"/></svg>
<p class="abs quote">" The leather club chair and crystal decanter set turned my basement into a true speakeasy in one weekend.<br><br>Every guest asks where the pieces came from, and the cigar humidor is simply stunning. "</p>
<div class="circle-btn" style="left:474px;top:3344px"><svg width="10" height="10" viewBox="0 0 10 10" fill="none" stroke="#fff" stroke-width="1.2"><path d="M9 5H1M4 2L1 5l3 3"/></svg></div>
<div class="circle-btn" style="left:513px;top:3344px"><svg width="10" height="10" viewBox="0 0 10 10" fill="none" stroke="#fff" stroke-width="1.2"><path d="M1 5h8M6 2l3 3-3 3"/></svg></div>
<a class="btn btn-ghost-dark" href="#" style="left:474px;top:3408px;width:114px;height:37px">View all</a>

<!-- everything handled -->
<h2 class="abs serif section-title" style="left:200px;top:3596px">We handle everything for you!</h2>
<div class="rule" style="left:0;top:3680px;width:364px;background:#333"></div>
<p class="abs" style="left:381px;top:3668px;width:580px;font-size:10px;line-height:18px">From choosing the right bar cart to delivering a full leather lounge set, our team guides every order so your home speakeasy arrives ready to pour and enjoy.</p>

<div class="feat" style="left:191px">
  <svg width="44" height="44" viewBox="0 0 44 44" fill="none" stroke="#000" stroke-width="1.6"><path d="M8 6h8l4 9-5 3a20 20 0 0 0 11 11l3-5 9 4v8a3 3 0 0 1-3 3C19 39 5 25 5 9a3 3 0 0 1 3-3z"/><path d="M28 4a12 12 0 0 1 12 12M28 10a6 6 0 0 1 6 6" stroke="var(--rose)"/></svg>
  One Call Away</div>
<div class="feat" style="left:396px">
  <svg width="44" height="44" viewBox="0 0 44 44" fill="none" stroke="#000" stroke-width="1.6"><rect x="6" y="6" width="28" height="34"/><path d="M12 2v8M20 2v8M28 2v8M11 18h16M11 24h16M11 30h10M32 28l8-8 2 2-8 8-3 1z"/></svg>
  Free Shipping Quote</div>
<div class="feat" style="left:602px">
  <svg width="44" height="44" viewBox="0 0 44 44" fill="none" stroke="#000" stroke-width="1.6"><path d="M8 24h8v16H8zM16 26l6-8 2-6h3v8h9l-2 20H16"/><path d="M10 8l2 3 3-1-2 3 2 3-3-1-2 3-1-3-3 1 2-3-2-3 3 1zM30 4l2 3 3-1-2 3 2 3-3-1-2 3-1-3-3 1 2-3-2-3 3 1z" stroke="var(--rose)"/></svg>
  Quality Guaranteed</div>
<div class="feat" style="left:809px">
  <svg width="44" height="44" viewBox="0 0 44 44" fill="none" stroke="#000" stroke-width="1.6"><path d="M8 24v-4a14 14 0 0 1 28 0v4"/><rect x="5" y="22" width="8" height="12" rx="2"/><rect x="31" y="22" width="8" height="12" rx="2"/><path d="M35 34c0 4-4 6-10 6"/></svg>
  Support After Purchase</div>
<a class="btn btn-ghost" href="#" style="left:532px;top:3845px;width:136px;height:37px">Contact Us Today!</a>

<!-- contact -->
<div class="photo" style="left:0;top:3956px;width:550px;height:500px;background:linear-gradient(120deg,#140c12 0%,#3a1822 40%,#8a2a2e 65%,#2a1014 100%)" role="img" aria-label="Woman in a red dress seated at a dark bar with a glass of whiskey"></div>
<section class="abs" style="left:550px;top:3956px;width:650px;height:500px;background:var(--blush)"></section>
<p class="abs" style="left:612px;top:4051px;font-size:10px;font-weight:600">Ready to get started?</p>
<h2 class="abs serif" style="left:612px;top:4076px;font-size:40px">Get in touch</h2>
<div class="field" style="left:612px;top:4152px;width:233px;height:34px">Name</div>
<div class="field" style="left:860px;top:4152px;width:232px;height:34px">Phone</div>
<div class="field" style="left:612px;top:4202px;width:480px;height:34px">Email</div>
<div class="field" style="left:612px;top:4251px;width:480px;height:60px">Message...</div>
<div class="btn" style="left:612px;top:4327px;width:112px;height:34px;background:#000;color:#fff">Submit</div>

<!-- footer -->
<section class="band dark" style="top:4456px;height:352px"></section>
<div class="abs" style="left:202px;top:4527px;width:134px;height:134px;border:2px solid var(--blush);border-radius:50%;display:flex;align-items:center;justify-content:center;color:var(--blush);font-size:15px;font-weight:500;text-align:center;line-height:1.3">Bourbon<br>Lantern</div>
<div class="abs foot-label" style="left:457px;top:4533px">Contact us <span></span></div>
<div class="abs foot-text" style="left:457px;top:4565px">+1 (555) - 018 - 2290<br>info@bourbonlantern.com</div>
<div class="social" style="left:457px"></div>
<div class="social" style="left:494px"></div>
<div class="social" style="left:532px;background:var(--blush)"></div>
<div class="social" style="left:571px"></div>
<div class="abs foot-label" style="left:769px;top:4533px">Address <span></span></div>
<div class="abs foot-text" style="left:769px;top:4565px">1927 Runner's Alley<br>Barrel Row, Cellar 4<br>4019 - Kentucky</div>
<div class="abs" style="left:200px;top:4736px;width:800px;height:1px;background:#333"></div>
<p class="abs" style="left:200px;top:4765px;font-size:9.5px;color:#bbb">© 2024 <b style="color:#fff">Bourbon Lantern</b>. All Right Reserved</p>
<svg class="abs" style="left:1084px;top:4760px" width="16" height="18" viewBox="0 0 16 18" fill="var(--blush)"><path d="M8 0l8 18-8-5-8 5z"/></svg>

</body>
</html>
```